Postcard for Direct Mail for a startup company

This will be a postcard for Direct Mail to Churches across America. The size should be around 4" x 6". The front should have our Logo (attached) with the following words:
Audio, Video and Lighting Equipment
Exclusive for churches
DEALER PRICING (This should be what stands out)
tessrin.org and perhaps a URCode.

The front should look trendy and Modern yet clean and sleek. Its important that the reader see "Dealer Pricing" and understand quickly it is for Audio, Video and Lighting equipment.

The back should have room for the Harlow Crest Postal information where a printer can print the address and such. It should also contain the description paragraph. (attached)

The fonts in the Logo are: SF New Republic and Outfit. This is for informational purposes only. You don't have to use these.

Target Market(s)

Churches / Houses of Worship

Requirements
Must have
• Trendy yet sleek and stylish (modern). Make sure the size works for bulk mailing and postcard.

```html
<!DOCTYPE html>
<html lang="en">
<head>
<meta charset="utf-8">
<title>Dealer Pricing Postcard</title>
<link href="https://fonts.googleapis.com/css2?family=Comfortaa:wght@700&family=Oswald:wght@600&family=Outfit:wght@500;700;800&display=swap" rel="stylesheet">
<style>
  :root {
    --ink-dark: #0b0712;
    --deep-blue: #1c1a8a;
    --violet: #3a2cc4;
    --crimson: #8e1016;
    --badge-yellow: #fff200;
    --badge-red: #e3141b;
    --banner-blue: #0a8ed8;
    --banner-light: #23b5f0;
    --accent-yellow: #f7e52a;
    --brand-blue: #1f7fd1;
    --white: #ffffff;
  }
  * { margin: 0; padding: 0; box-sizing: border-box; }
  html, body { width: 1200px; height: 800px; overflow: hidden; background: var(--ink-dark); }
  .postcard { position: relative; width: 1200px; height: 800px; overflow: hidden; }

  .hero-photo {
    position: absolute; inset: 0;
    background:
      radial-gradient(ellipse 55% 40% at 40% 25%, rgba(90,80,255,0.55), transparent 70%),
      radial-gradient(ellipse 45% 35% at 80% 45%, rgba(70,60,230,0.6), transparent 70%),
      radial-gradient(ellipse 40% 45% at 100% 95%, rgba(180,20,25,0.9), transparent 70%),
      radial-gradient(ellipse 60% 40% at 20% 60%, rgba(150,40,120,0.5), transparent 70%),
      linear-gradient(180deg, #1a1560 0%, #2a1f9a 35%, #3c1e6e 60%, #2a0c1e 85%, var(--ink-dark) 100%);
  }

  .price-badge { position: absolute; left: 23px; top: 23px; width: 300px; height: 300px; }
  .price-badge .halo {
    position: absolute; inset: 0; border-radius: 50%;
    background: radial-gradient(circle, rgba(255,242,0,0.55) 55%, rgba(255,242,0,0.15) 80%, transparent 100%);
  }
  .price-badge .disc {
    position: absolute; left: 50px; top: 50px; width: 200px; height: 200px; border-radius: 50%;
    background: var(--badge-yellow);
    display: flex; align-items: center; justify-content: center; flex-direction: column;
  }
  .price-badge .label {
    font-family: 'Oswald', sans-serif; font-weight: 600; color: var(--badge-red);
    font-size: 58px; line-height: 50px; text-align: center; letter-spacing: -1px;
  }

  .headline {
    position: absolute; left: 68px; top: 400px;
    font-family: 'Comfortaa', sans-serif; font-weight: 700; color: var(--white);
    font-size: 82px; line-height: 87px; letter-spacing: 1px; white-space: nowrap;
  }

  .audience-banner {
    position: absolute; left: 72px; top: 680px; width: 465px; height: 53px;
    background: linear-gradient(90deg, var(--banner-blue), var(--banner-light) 60%, var(--banner-blue));
    clip-path: polygon(4% 0, 100% 0, 96% 100%, 0 100%);
    display: flex; align-items: center; padding-left: 35px;
    font-family: 'Outfit', sans-serif; font-weight: 700; font-size: 29px; color: var(--white);
  }
  .audience-banner .highlight { color: var(--accent-yellow); margin-right: 10px; }

  .brand-name {
    position: absolute; left: 900px; top: 545px;
    font-family: 'Outfit', sans-serif; font-weight: 700; font-size: 78px; color: var(--brand-blue);
    letter-spacing: -1px;
  }

  .web-address {
    position: absolute; left: 900px; top: 697px; display: flex; align-items: center; gap: 12px;
    font-family: 'Outfit', sans-serif; font-weight: 800; font-size: 32px; color: var(--white);
  }
  .web-address svg { width: 40px; height: 40px; }
</style>
</head>
<body>
<main class="postcard">
  <div class="hero-photo" role="img" aria-label="Close-up of a hand on a lit DJ mixing controller with knobs and jog wheels in blue and red light"></div>

  <div class="price-badge">
    <div class="halo"></div>
    <div class="disc"><p class="label">DEALER<br>PRICING</p></div>
  </div>

  <h1 class="headline">AUDIO, VIDEO<br>AND LIGHTING<br>EQUIPMENT</h1>

  <p class="audience-banner"><span class="highlight">EXCLUSIVE</span>FOR CHURCHES</p>

  <p class="brand-name">tessrin</p>

  <p class="web-address">tessrin.org
    <svg viewBox="0 0 40 40" aria-hidden="true">
      <g stroke="var(--accent-yellow)" stroke-width="2" stroke-linecap="round">
        <line x1="10" y1="2" x2="10" y2="8"/>
        <line x1="2" y1="12" x2="7" y2="12"/>
        <line x1="4" y1="5" x2="7" y2="8"/>
        <line x1="4" y1="20" x2="7" y2="17"/>
        <line x1="17" y1="5" x2="14" y2="8"/>
      </g>
      <path d="M12 12 L34 22 L24 24 L31 34 L28 36 L21 26 L15 32 Z" fill="var(--white)" stroke="#6a8fc0" stroke-width="1"/>
    </svg>
  </p>
</main>
</body>
</html>
```